Silver Ridge Business Card Design

I have an existing corporate logo. I'd like to clean it up bit (sharpen it up) and make it look better (without major redesign). I'd like to get the logo itself in all major file formats for print, web, etc.
Then I'd like a business card design that reflects a strategy consulting firm. It should be clean - logo and text without major graphics, and perhaps some small color treatments that match the logo color. The card should suggest high quality in terms of the company.
I'd like the files for card in all major print formats.
Target Market(s)
Silver Ridge Partners is a strategy development and business consulting firm focused on small to mid-sized companies. We specialize in business strategy, comprehensive business plan development, market segmentation and positioning, financial models, marketing and sales strategy, product strategy and the effective use of social media in business growth. We operate as consultants, advisers, retained members of management teams, and Board members. We often serve in the role of Chief Strategy Officer, supporting CEO's and other senior executives to enhance top and bottom line growth.
Our overall approach with clients is to deliver actual results, and we often take an active team role with business founders and management teams to drive business growth and affect real changes in performance. As a result, we approach each situation uniquely and partner with clients in a manner that will have the biggest impact on enterprise value.
Business
Look and feel

```html
<!DOCTYPE html>
<html lang="en">
<head>
<meta charset="utf-8">
<title>Silver Ridge Partners – Business Card</title>
<link rel="stylesheet" href="https://fonts.googleapis.com/css2?family=Exo+2:wght@400;500;700&display=swap">
<style>
  :root {
    --page-bg: #e9e9eb;
    --card-white: #ffffff;
    --card-shade: #eeeeef;
    --charcoal: #343436;
    --navy: #263a7a;
    --text-muted: #4a4a50;
  }
  html, body {
    margin: 0;
    width: 1200px;
    height: 900px;
    overflow: hidden;
    background: var(--page-bg);
    font-family: "Exo 2", "Segoe UI", sans-serif;
  }
  .stage {
    width: 1200px;
    height: 900px;
    display: flex;
    align-items: center;
    justify-content: center;
  }
  .business-card {
    position: relative;
    width: 1000px;
    height: 572px;
    border-radius: 44px;
    overflow: hidden;
    background: radial-gradient(ellipse at 40% 45%, var(--card-white) 55%, var(--card-shade) 100%);
    box-shadow: 0 18px 40px rgba(0,0,0,0.18);
  }
  .card-art {
    position: absolute;
    inset: 0;
    width: 100%;
    height: 100%;
  }
  .card-art .band-dark { fill: var(--charcoal); }
  .card-art .band-navy { fill: var(--navy); }

  .company-name {
    position: absolute;
    left: 110px;
    top: 82px;
    margin: 0;
    color: var(--navy);
    font-weight: 700;
    font-size: 30px;
    line-height: 1.08;
    letter-spacing: 1.5px;
    text-transform: uppercase;
  }

  .holder {
    position: absolute;
    right: 64px;
    top: 64px;
    text-align: right;
    color: #ffffff;
  }
  .holder-name {
    margin: 0;
    font-weight: 500;
    font-size: 30px;
    letter-spacing: 1.5px;
    text-transform: uppercase;
  }
  .holder-title {
    margin: 4px 0 0;
    font-weight: 400;
    font-size: 22px;
    letter-spacing: 0.5px;
  }

  .contact-list {
    position: absolute;
    left: 48px;
    top: 200px;
    margin: 0;
    padding: 0;
    list-style: none;
  }
  .contact-list li {
    display: flex;
    align-items: center;
    gap: 12px;
    height: 34px;
    color: var(--text-muted);
    font-size: 18px;
    letter-spacing: 0.6px;
  }
  .contact-icon {
    width: 20px;
    height: 20px;
    flex: none;
  }
  .contact-icon .disc { fill: var(--navy); }
  .contact-icon .glyph { fill: #ffffff; }
  .contact-icon .glyph-line { fill: none; stroke: #ffffff; stroke-width: 1.4; }
  .contact-icon .glyph-cut { fill: none; stroke: var(--navy); stroke-width: 1.2; }
  .contact-icon .glyph-dot { fill: var(--navy); }
</style>
</head>
<body>
<main class="stage">
  <article class="business-card">
    <svg class="card-art" viewBox="0 0 1000 572" preserveAspectRatio="none" aria-hidden="true">
      <path class="band-dark" d="M230,0 L1000,0 L1000,572 L870,572 C830,260 620,40 230,0 Z"/>
      <path class="band-navy" d="M160,0 C560,30 790,250 832,572 L860,572 C818,270 610,50 200,0 Z"/>
    </svg>

    <h1 class="company-name">Silver Ridge<br>Partners, LLC</h1>

    <div class="holder">
      <p class="holder-name">Daniel Whitmore</p>
      <p class="holder-title">Managing Director</p>
    </div>

    <ul class="contact-list">
      <li>
        <svg class="contact-icon" viewBox="0 0 20 20" aria-hidden="true"><circle class="disc" cx="10" cy="10" r="10"/><path class="glyph" d="M7,5 L9,5 L9.6,8 L8.4,9 C9,10.4 9.8,11.2 11,11.6 L12,10.4 L15,11 L15,13 C15,14 14,14.6 13,14.4 C9.4,13.6 6.4,10.6 5.6,7 C5.4,6 6,5 7,5 Z"/></svg>
        <span>014 552 3087</span>
      </li>
      <li>
        <svg class="contact-icon" viewBox="0 0 20 20" aria-hidden="true"><circle class="disc" cx="10" cy="10" r="10"/><rect class="glyph" x="7" y="4.5" width="6" height="11" rx="1"/></svg>
        <span>014 552 3091</span>
      </li>
      <li>
        <svg class="contact-icon" viewBox="0 0 20 20" aria-hidden="true"><circle class="disc" cx="10" cy="10" r="10"/><rect class="glyph" x="5" y="6.5" width="10" height="7" rx="1"/><path class="glyph-cut" d="M5.5,7 L10,10.5 L14.5,7"/></svg>
        <span>d.whitmore@silverridge.co</span>
      </li>
      <li>
        <svg class="contact-icon" viewBox="0 0 20 20" aria-hidden="true"><circle class="disc" cx="10" cy="10" r="10"/><circle class="glyph-line" cx="10" cy="10" r="5"/><path class="glyph-line" d="M5,10 L15,10 M10,5 C7.5,8 7.5,12 10,15 M10,5 C12.5,8 12.5,12 10,15"/></svg>
        <span>www.silverridge.co</span>
      </li>
      <li>
        <svg class="contact-icon" viewBox="0 0 20 20" aria-hidden="true"><circle class="disc" cx="10" cy="10" r="10"/><path class="glyph" d="M10,4 C12.5,4 14,5.8 14,8 C14,10.8 10,15.5 10,15.5 C10,15.5 6,10.8 6,8 C6,5.8 7.5,4 10,4 Z"/><circle class="glyph-dot" cx="10" cy="8" r="1.5"/></svg>
        <span>214 North Elm Street, Suite 9</span>
      </li>
    </ul>
  </article>
</main>
</body>
</html>
```